Louisiana personal injury attorney needs a postcard design

This will be the first of three post cards to go out to previous clients. We do not have intentions of making all three match/work with each other, but if you have an idea for that, please, let us know! This is for an attorney in Lafayette, LA that specializes in Medical Malpractice and Personal Injury. We would like the front of the post card to focus on those two practice areas and really grab someones attention!

the card in general will say: Glad to have served you, come see us for a free T-shirt, have a cup of coffee with us…

Please use a photo of the office for us to use on the back with a map of the office location (will send location when we pick the winner)

Industry/Entity Type

Legal

Font styles to use
Serif
Sans Serif

Requirements
Must have
• map of location of office. Large image or several images on the front. attention grabbing
Nice to have
• colors that match the logo. clean and easy to follow
Should not have
• should not be messy or too much going on.

```html
<!DOCTYPE html>
<html lang="en">
<head>
<meta charset="utf-8">
<title>Bellmont Law Firm Postcard</title>
<link href="https://fonts.googleapis.com/css2?family=Oswald:wght@400;500&family=Open+Sans:wght@400;600;700&display=swap" rel="stylesheet">
<style>
  :root {
    --gold: #c99a35;
    --gold-text: #d9a52c;
    --charcoal: #3a3a3c;
    --mid-grey: #6d6e70;
    --light-grey: #ececec;
    --backdrop: #6b6b6b;
    --white: #ffffff;
    --ink: #444446;
  }
  * { box-sizing: border-box; margin: 0; padding: 0; }
  html, body { width: 929px; height: 1200px; overflow: hidden; background: var(--backdrop); }
  .stage { position: relative; width: 981px; height: 1268px; transform: scale(0.947); transform-origin: 0 0; }
  .card { position: absolute; left: 128px; width: 700px; height: 500px; background: var(--white); overflow: hidden; font-family: "Open Sans", sans-serif; box-shadow: 0 4px 12px rgba(0,0,0,.35); }
  .card--front { top: 108px; }
  .card--back { top: 680px; }
  .abs { position: absolute; }
  .heading { font-family: "Oswald", sans-serif; font-weight: 500; color: var(--white); font-size: 25px; letter-spacing: .3px; }

  /* front */
  .front-brand { left: 0; top: 0; width: 400px; height: 130px; background: var(--gold); }
  .brand-name { font-family: "Open Sans", sans-serif; font-weight: 700; color: var(--white); text-align: center; line-height: 1; }
  .front-brand .brand-name { left: 30px; top: 28px; width: 260px; font-size: 40px; }
  .front-brand .brand-name span { display: block; font-size: 24px; letter-spacing: 6px; margin-top: 8px; }
  .photo-crash { left: 360px; top: 0; width: 340px; height: 290px; background: linear-gradient(160deg, #b9b4ad, #5f6468 55%, #8c8a86); clip-path: polygon(32px 0, 100% 0, 100% 100%, 0 100%, 0 85%); }
  .slash { left: 340px; top: 0; width: 52px; height: 290px; background: var(--white); clip-path: polygon(40px 0, 52px 0, 12px 100%, 0 100%); }
  .front-band { left: 0; top: 130px; width: 350px; height: 92px; background: var(--charcoal); clip-path: polygon(0 0, 100% 0, 91% 100%, 0 100%); padding: 10px 0 0 21px; }
  .front-band .sub { font-weight: 700; color: var(--gold-text); font-size: 14px; line-height: 20px; margin-top: 6px; }
  .front-tag { left: 0; top: 222px; width: 320px; height: 68px; background: var(--gold); clip-path: polygon(0 0, 100% 0, 94% 100%, 0 100%); padding: 14px 0 0 21px; color: var(--white); font-size: 17px; line-height: 20px; font-weight: 600; }
  .rule-grey { left: 0; top: 290px; width: 700px; height: 6px; background: var(--mid-grey); }
  .photo-doctors { left: 0; top: 296px; width: 330px; height: 204px; background: linear-gradient(135deg, #dfe3e6, #8fb6cf 50%, #e8e8ea); clip-path: polygon(0 0, 100% 0, 88% 100%, 0 100%); }
  .services { left: 300px; top: 296px; width: 400px; height: 204px; background: var(--light-grey); clip-path: polygon(30px 0, 100% 0, 100% 100%, 8px 100%); }
  .services-title { left: 316px; top: 322px; font-weight: 700; color: var(--gold-text); font-size: 17px; }
  .check-list { left: 316px; top: 352px; width: 380px; display: grid; grid-template-columns: 167px 1fr; row-gap: 7px; list-style: none; }
  .check-list li { font-size: 12.5px; color: var(--ink); display: flex; align-items: center; gap: 4px; height: 18px; }
  .web-band { left: 312px; top: 458px; width: 180px; height: 27px; background: var(--mid-grey); color: var(--white); font-weight: 700; font-size: 11.5px; line-height: 27px; padding-left: 20px; clip-path: polygon(0 0, 100% 0, 92% 100%, 0 100%); }
  .cta-band { left: 480px; top: 438px; width: 220px; height: 62px; background: var(--gold); clip-path: polygon(18px 0, 100% 0, 100% 100%, 0 100%); }
  .cta-label { font-family: "Oswald", sans-serif; font-size: 11px; color: var(--charcoal); }
  .phone-line { font-family: "Oswald", sans-serif; font-size: 16px; color: var(--white); display: flex; align-items: center; gap: 5px; }
  .cta-band .cta-label { left: 32px; top: 10px; }
  .cta-band .phone-line { left: 6px; top: 32px; }

  /* back */
  .photo-office { left: 0; top: 0; width: 350px; height: 175px; background: linear-gradient(180deg, #8fb4d8, #c9d7e0 40%, #3e3f44 55%, #5b7a45); clip-path: polygon(0 0, 92% 0, 100% 100%, 0 100%); }
  .back-band { left: 0; top: 172px; width: 390px; height: 78px; background: var(--charcoal); padding: 12px 0 0 21px; box-shadow: 0 3px 5px rgba(0,0,0,.3); }
  .back-band .sub { color: var(--gold-text); font-size: 15px; margin-top: 2px; }
  .back-gold { left: 0; top: 250px; width: 395px; height: 112px; background: var(--gold); clip-path: polygon(0 0, 97% 0, 100% 100%, 0 100%); }
  .photo-room { left: 12px; top: 250px; width: 122px; height: 122px; border-radius: 50%; border: 4px solid var(--white); background: linear-gradient(160deg, #9cb3c4, #5d6b78 55%, #d8cbb0); box-shadow: 0 2px 6px rgba(0,0,0,.4); }
  .welcome { left: 155px; top: 272px; width: 235px; color: var(--white); font-size: 16px; line-height: 21px; }
  .map { left: 0; top: 360px; width: 420px; height: 100px; background: linear-gradient(120deg, #eef0ee, #dfe4e0 60%, #e9ebe8); clip-path: polygon(0 0, 97% 0, 100% 100%, 0 100%); }
  .back-cta { left: 0; top: 438px; width: 220px; height: 62px; background: var(--charcoal); clip-path: polygon(0 0, 92% 0, 100% 100%, 0 100%); }
  .back-cta .cta-label { left: 9px; top: 11px; color: var(--gold-text); }
  .back-cta .phone-line { left: 8px; top: 32px; }
  .back-web { left: 215px; top: 460px; width: 205px; height: 25px; background: var(--mid-grey); color: var(--white); font-weight: 700; font-size: 11px; line-height: 25px; padding-left: 40px; clip-path: polygon(0 0, 100% 0, 97% 100%, 0 100%); }
  .return-address { left: 398px; top: 30px; font-size: 12.5px; color: var(--ink); line-height: 16px; }
  .return-address strong { display: block; color: var(--gold-text); font-size: 15px; font-weight: 600; margin-bottom: 1px; }
  .stamp-box { left: 587px; top: 23px; width: 97px; height: 72px; border: 1.5px solid #c9c9c9; }
  .address-line { left: 405px; width: 275px; height: 1.5px; background: #cfcfcf; }
  .back-logo { left: 470px; top: 420px; width: 215px; font-size: 40px; color: var(--gold); }
  .back-logo span { display: block; font-size: 22px; letter-spacing: 6px; margin-top: 6px; }
</style>
</head>
<body>
<div class="stage">

  <section class="card card--front">
    <div class="abs photo-crash" role="img" aria-label="Photo of emergency crews at a car accident scene"></div>
    <div class="abs slash"></div>
    <div class="abs front-brand">
      <div class="abs brand-name">BELLMONT<span>LAW FIRM</span></div>
    </div>
    <div class="abs front-band">
      <h1 class="heading">GET THE LEGAL HELP YOU NEED!!</h1>
      <p class="sub">SPECIALIZES IN MEDICAL MALPRACTICE<br>AND PERSONAL INJURY!</p>
    </div>
    <div class="abs front-tag">Experienced Louisiana<br>Personal Injury Attorneys</div>
    <div class="abs rule-grey"></div>
    <div class="abs services"></div>
    <div class="abs photo-doctors" role="img" aria-label="Overhead photo of a medical team reviewing scans"></div>
    <h2 class="abs services-title">DEDICATED TO HELPING INJURED PEOPLE</h2>
    <ul class="abs check-list">
      <li><svg width="13" height="13" viewBox="0 0 13 13"><rect x="1" y="2" width="10" height="10" fill="none" stroke="#6d6e70" stroke-width="1.2"/><path d="M3 7l2.5 2.5L12 2" fill="none" stroke="#c99a35" stroke-width="1.8"/></svg>Motor vehicle accidents</li>
      <li><svg width="13" height="13" viewBox="0 0 13 13"><rect x="1" y="2" width="10" height="10" fill="none" stroke="#6d6e70" stroke-width="1.2"/><path d="M3 7l2.5 2.5L12 2" fill="none" stroke="#c99a35" stroke-width="1.8"/></svg>Workplace accidents</li>
      <li><svg width="13" height="13" viewBox="0 0 13 13"><rect x="1" y="2" width="10" height="10" fill="none" stroke="#6d6e70" stroke-width="1.2"/><path d="M3 7l2.5 2.5L12 2" fill="none" stroke="#c99a35" stroke-width="1.8"/></svg>Maritime injuries</li>
      <li><svg width="13" height="13" viewBox="0 0 13 13"><rect x="1" y="2" width="10" height="10" fill="none" stroke="#6d6e70" stroke-width="1.2"/><path d="M3 7l2.5 2.5L12 2" fill="none" stroke="#c99a35" stroke-width="1.8"/></svg>Dangerous or defective products</li>
      <li><svg width="13" height="13" viewBox="0 0 13 13"><rect x="1" y="2" width="10" height="10" fill="none" stroke="#6d6e70" stroke-width="1.2"/><path d="M3 7l2.5 2.5L12 2" fill="none" stroke="#c99a35" stroke-width="1.8"/></svg>Medical malpractice</li>
      <li><svg width="13" height="13" viewBox="0 0 13 13"><rect x="1" y="2" width="10" height="10" fill="none" stroke="#6d6e70" stroke-width="1.2"/><path d="M3 7l2.5 2.5L12 2" fill="none" stroke="#c99a35" stroke-width="1.8"/></svg>Premises liability</li>
    </ul>
    <div class="abs web-band">WWW.BELLMONTLAW.COM</div>
    <div class="abs cta-band">
      <div class="abs cta-label">GET A FREE INITIAL CONSULTATION</div>
      <div class="abs phone-line"><svg width="18" height="18" viewBox="0 0 18 18"><path d="M4 2h4l1 4-2 1.5a9 9 0 0 0 3.5 3.5L12 9l4 1v4c0 1-1 2-2 2A12 12 0 0 1 2 4c0-1 1-2 2-2z" fill="#fff"/></svg>800-555-0142 | 337-555-0176</div>
    </div>
  </section>

  <section class="card card--back">
    <div class="abs photo-office" role="img" aria-label="Photo of the firm's office building exterior"></div>
    <div class="abs back-gold"></div>
    <div class="abs back-band">
      <h2 class="heading">GET THE LEGAL HELP YOU NEED!!</h2>
      <p class="sub">Medical Malpractice and Personal Injury</p>
    </div>
    <div class="abs photo-room" role="img" aria-label="Photo of the office conference room"></div>
    <p class="abs welcome">Glad to have served you, come see us for a free T-shirt, have a cup of coffee with us…</p>
    <div class="abs map" role="img" aria-label="Street map showing the office location in Lafayette"></div>
    <div class="abs back-cta">
      <div class="abs cta-label">GET A FREE INITIAL CONSULTATION</div>
      <div class="abs phone-line"><svg width="18" height="18" viewBox="0 0 18 18"><path d="M4 2h4l1 4-2 1.5a9 9 0 0 0 3.5 3.5L12 9l4 1v4c0 1-1 2-2 2A12 12 0 0 1 2 4c0-1 1-2 2-2z" fill="#fff"/></svg>800-555-0142 | 337-555-0176</div>
    </div>
    <div class="abs back-web">WWW.BELLMONTLAW.COM</div>
    <address class="abs return-address" style="font-style:normal">
      <strong>BELLMONT LAW FIRM</strong>
      220 Cypress Court<br>Lafayette, LA 70508
    </address>
    <div class="abs stamp-box"></div>
    <div class="abs address-line" style="top:172px"></div>
    <div class="abs address-line" style="top:220px"></div>
    <div class="abs address-line" style="top:268px"></div>
    <div class="abs brand-name back-logo">BELLMONT<span>LAW FIRM</span></div>
  </section>

</div>
</body>
</html>
```